Gutschein Design Weihnachtsaktion Mähroboter
Zielgruppe
Installation für Mähroboter
Aufgabenstellung
Format DIN Lang (99x120mm) quer
Gutschein zur Installation eines Mähroboters
Auswahlfelder: für oberirdische oder unterirdische Verlegung
Auswahlfelder: bis 250m²; bis 500m², bis 1.000m²
Adressfeld/Namensfeld für den beschenkten
Serienfeld für Gutscheinnummer
Datums und Unterschriftsfeld
Design Vorstellung: Ein Männchen welches einen Mähroboter installiert, Design Mähroboter mit Weihnachtsmütze.... / Weihnachtliche Grundgestaltung. Sind für Ideen offen!
unser Logo integrieren

```html
<!DOCTYPE html>
<html lang="de">
<head>
<meta charset="utf-8">
<title>Gutschein Mähroboter-Installation</title>
<link rel="stylesheet" href="https://fonts.googleapis.com/css2?family=Roboto:wght@300;500&display=swap">
<style>
  :root {
    --table-dark: #3a2416;
    --table-mid: #5e3a24;
    --board-light: #e9c99a;
    --board-mid: #d9ad72;
    --board-edge: #b88447;
    --ink: #2e2620;
    --line: #3b312a;
    --brand: #ef7d22;
  }
  * { margin: 0; padding: 0; box-sizing: border-box; }
  html, body { width: 1200px; height: 990px; overflow: hidden; }
  body { font-family: "Roboto", Arial, sans-serif; font-weight: 300; color: var(--ink); }
  .voucher { position: relative; width: 1200px; height: 990px; overflow: hidden; }
  .table-scene {
    position: absolute; inset: 0;
    background: radial-gradient(ellipse at 40% 30%, var(--table-mid), var(--table-dark) 75%);
  }
  .board { position: absolute; inset: 0; }
  .form {
    position: absolute; left: 0; top: 0; width: 1200px; height: 990px;
    transform: rotate(-2.5deg); transform-origin: 104px 368px;
  }
  .label { position: absolute; font-size: 22px; line-height: 1; white-space: nowrap; }
  .field { position: absolute; border: 1.5px solid var(--line); height: 34px; }
  .rule { position: absolute; border-top: 1.5px solid var(--line); }
  .check { display: inline-block; width: 19px; height: 19px; border: 1.5px solid var(--line); vertical-align: -2px; margin-right: 6px; }
  .brand { position: absolute; left: 100px; top: 738px; width: 190px; display: flex; align-items: center; gap: 10px; }
  .brand-mark { flex: none; width: 22px; height: 22px; background: var(--brand); }
  .brand-name { font-size: 30px; font-weight: 500; line-height: 1.05; color: var(--brand); }
  .contact { position: absolute; left: 312px; top: 784px; font-size: 22px; white-space: nowrap; }
  .web { position: absolute; left: 312px; top: 816px; font-size: 20px; font-weight: 500; color: var(--brand); white-space: nowrap; }
</style>
</head>
<body>
<main class="voucher">
  <div class="table-scene" role="img" aria-label="Dunkler Holztisch mit Kochlöffel, Tannenzweig mit roten Beeren, Sternanis, getrockneter Orangenscheibe und Zimtstangen"></div>

  <svg class="board" viewBox="0 0 1200 990" role="img" aria-label="Helles Holzschneidebrett als Gutscheinfläche">
    <defs>
      <linearGradient id="boardTone" x1="0" y1="0" x2="1" y2="1">
        <stop offset="0" stop-color="var(--board-light)"/>
        <stop offset="0.6" stop-color="var(--board-mid)"/>
        <stop offset="1" stop-color="var(--board-edge)"/>
      </linearGradient>
    </defs>
    <path d="M15 305 L1100 256 L1140 262 L1185 330 L1200 600 L1195 780 L1130 872 L20 918 Z" fill="url(#boardTone)"/>
    <circle cx="1101" cy="559" r="21" fill="var(--table-dark)"/>
  </svg>

  <section class="form">
    <span class="label" style="left:104px;top:352px">Modell:</span>
    <div class="field" style="left:307px;top:337px;width:180px;height:36px"></div>
    <span class="label" style="left:764px;top:352px">Gutschein Nr.:</span>

    <span class="label" style="left:106px;top:408px">Name, Vorname:</span>
    <div class="field" style="left:310px;top:398px;width:680px"></div>

    <span class="label" style="left:108px;top:462px">Straße, Haus-Nr.:</span>
    <div class="field" style="left:312px;top:452px;width:680px"></div>

    <span class="label" style="left:110px;top:516px">PLZ, Ort:</span>
    <div class="field" style="left:314px;top:506px;width:680px"></div>

    <span class="label" style="left:112px;top:566px">Art der Installation:</span>
    <span class="label" style="left:318px;top:566px"><span class="check"></span>Oberirdisch</span>
    <span class="label" style="left:512px;top:566px"><span class="check"></span>Unterirdisch</span>

    <span class="label" style="left:114px;top:618px">Größe der Rasenfläche:</span>
    <span class="label" style="left:374px;top:618px"><span class="check"></span>0 bis 250m²</span>
    <span class="label" style="left:540px;top:618px"><span class="check"></span>251 bis 500m²</span>
    <span class="label" style="left:756px;top:618px"><span class="check"></span>501 bis 1.000m²</span>

    <span class="label" style="left:306px;top:690px">Datum:</span>
    <div class="rule" style="left:388px;top:712px;width:222px"></div>
    <span class="label" style="left:635px;top:690px">Unterschrift:</span>
    <div class="rule" style="left:772px;top:712px;width:221px"></div>

    <div class="brand"><span class="brand-mark"></span><span class="brand-name">Rasenwerk<br>Nord</span></div>
    <span class="contact">+49 (0) 4021 558310 &nbsp;|&nbsp; info@rasenwerk-nord.de</span>
    <span class="web">www.rasenwerk-nord.de</span>
  </section>
</main>
</body>
</html>
```